Modern Corporate Brochure For Australian Real Estate Agency

We need a corporate 10 page A4 brochure for a Australian Real Estate agency with information for our clients and referral partners.

Main colour scheme: #238b53

Examples of designs:
https://plorvendax.example/item/8-page-corporate-business-brochure/5820417

https://plorvendax.example/item/brochure/7461283

https://plorvendax.example/item/the-company-profile/39851620

https://plorvendax.example/item/brochure-pack-a4trifold-leafletbusiness-card/857312

Target Market(s)

Professional Australians

Industry/Entity Type

Real Estate

Font styles to use
Sans Serif

Requirements
Must have
• Use of multiple greens from the logo

```html
<!DOCTYPE html>
<html lang="en">
<head>
<meta charset="utf-8">
<title>KDR Property Group – Brochure Spreads</title>
<link rel="stylesheet" href="https://fonts.googleapis.com/css2?family=Roboto:ital,wght@0,300;0,400;0,500;0,700;1,400&family=Roboto+Condensed:wght@700&display=swap">
<style>
  :root{
    --green:#238b53;
    --green-bright:#2ea34a;
    --green-dark:#17683c;
    --green-deep:#0f5535;
    --charcoal:#3a3a3a;
    --grey:#7b7b7b;
    --grey-light:#b9b9b9;
    --text:#333333;
    --paper:#ffffff;
  }
  *{margin:0;padding:0;box-sizing:border-box}
  html,body{width:780px;height:1200px;overflow:hidden;background:#fff}
  body{position:relative;font-family:"Roboto",Arial,sans-serif;color:var(--text)}
  .spread{position:absolute;left:19px;width:742px;height:576px;background:var(--paper);border:1px solid #555;overflow:hidden}
  .spread--cover{top:17px}
  .spread--inside{top:611px}
  .spread__shapes{position:absolute;inset:0;width:100%;height:100%}
  .abs{position:absolute}
  .condensed{font-family:"Roboto Condensed","Arial Narrow",sans-serif;font-weight:700}

  /* cover */
  .cover-title{right:387px;top:37px;text-align:right;font-size:35px;line-height:33px;color:var(--charcoal)}
  .cover-title span{display:block}
  .cover-title .light{color:var(--green-dark);font-weight:400}
  .cover-title .bold{font-weight:700}
  .cover-kicker{right:388px;top:135px;text-align:right;font-size:12px;line-height:14.5px;color:var(--green-dark)}
  .cover-body{left:72px;top:214px;width:286px;font-size:12.9px;line-height:16.4px;text-align:justify}
  .dots{left:178px;top:343px;display:flex;gap:3px}
  .dots i{width:7px;height:7px;border-radius:50%;background:var(--green-dark)}
  .dots i:nth-child(2){background:var(--green-bright)}
  .photo-circle{position:absolute;border-radius:50%;border:3px solid #fff;box-shadow:0 0 0 1px #ddd}
  .address{left:217px;top:372px;font-size:12.6px;line-height:14.6px}
  .address h3{font-weight:400;font-size:16px;color:var(--green-bright);line-height:18px}
  .address p{margin-bottom:14px}
  .address .phone{font-weight:700;color:var(--green-dark);font-size:13.6px;margin-top:-2px}
  .band-note{left:47px;top:517px;font-size:12px;line-height:15px;color:#fff}
  .band-note strong{color:var(--green-bright)}
  .grey-band-text{left:389px;top:321px;font-size:16.5px;line-height:20px;color:#fff}
  .grey-band-text strong{font-weight:700}
  .brand{left:545px;top:84px;font-size:13.5px;font-weight:500;color:var(--green-dark);letter-spacing:.2px}
  .cover-slogan{right:19px;top:447px;text-align:right;color:var(--charcoal)}
  .cover-slogan .big{font-size:33px;line-height:32px;display:block}
  .cover-slogan .small{font-size:16px;letter-spacing:4px;color:var(--green-dark);display:block;margin-top:3px}

  /* inside */
  .inside-title{right:385px;top:26px;text-align:right;font-size:33px;line-height:33px}
  .inside-title .light{font-weight:300;color:var(--charcoal);display:block}
  .inside-title .bold{font-weight:700;color:var(--green-dark);display:block}
  .inside-sub{right:385px;top:150px;text-align:right;font-size:13px;line-height:16.5px;font-weight:700;color:var(--charcoal)}
  .inside-body{left:87px;top:219px;width:286px;font-size:10.4px;line-height:14.5px;text-align:justify}
  .inside-body .last{text-align:right}
  .donate{left:28px;top:442px;width:324px;text-align:center}
  .donate h3{font-size:16px;color:var(--green-dark);font-weight:700;line-height:18px}
  .donate p{font-size:10.8px;line-height:15px;margin-top:2px}
  .pay-band{left:102px;top:521px;font-size:21px;line-height:26px;color:#fff;white-space:nowrap}
  .pay-band strong{color:var(--green-bright)}
  .col-title{left:388px;top:30px;font-size:19.5px;font-weight:700;color:var(--green-dark);line-height:21px}
  .col-sub{left:388px;top:52px;font-size:16px;color:var(--charcoal)}
  .quote{left:388px;top:86px;width:169px;font-size:10.1px;line-height:12.8px;text-align:justify}
  .bullets{left:388px;top:281px;list-style:none;font-size:12.6px;line-height:20px}
  .bullets li::before{content:"•";margin-right:4px}
  .tagline{left:396px;top:364px;font-style:italic;color:var(--green-dark);font-size:12px}
  .col-para{left:388px;top:387px;width:192px;font-size:10px;line-height:12.8px;text-align:justify}
  .col-close{left:388px;top:469px;width:350px;font-size:16px;line-height:17px;white-space:nowrap}
</style>
</head>
<body>

<section class="spread spread--cover">
  <svg class="spread__shapes" viewBox="0 0 1180 916" preserveAspectRatio="none">
    <defs>
      <linearGradient id="leftTone" x1="0" y1="0" x2="1" y2="1">
        <stop offset="0" stop-color="var(--green-dark)"/><stop offset=".5" stop-color="var(--green-bright)"/><stop offset="1" stop-color="var(--charcoal)"/>
      </linearGradient>
      <linearGradient id="rightTone" x1="1" y1="0" x2="0" y2="1">
        <stop offset="0" stop-color="var(--green-dark)"/><stop offset=".45" stop-color="var(--green-bright)"/><stop offset="1" stop-color="var(--green-deep)"/>
      </linearGradient>
    </defs>
    <polygon points="0,0 175,0 230,120 150,262 0,262" fill="url(#leftTone)" role="img" aria-label="Decorative green geometric panel"/>
  </svg>

  <div class="abs" role="img" aria-label="Illustration of city skyscrapers" style="left:371px;top:30px;width:158px;height:426px;background:linear-gradient(90deg,#2b2b2b,#6d6d6d 40%,#e6e6e6 55%,#3a3a3a 75%,#9a9a9a)"></div>

  <svg class="spread__shapes" viewBox="0 0 1180 916" preserveAspectRatio="none">
    <polygon points="895,250 1010,178 1180,178 1180,470 1065,640 800,760 700,916 590,916 590,820 720,620 880,478 895,325" fill="url(#rightTone)" role="img" aria-label="Decorative green geometric panel"/>
    <rect x="590" y="472" width="395" height="148" fill="var(--grey)"/>
    <polygon points="70,808 590,808 590,892 20,892" fill="var(--green-dark)"/>
  </svg>

  <h1 class="abs cover-title"><span class="light">WHY DO</span><span class="bold">WE USE IT?</span></h1>
  <p class="abs cover-kicker condensed">THE STANDARD CHUNK OF<br>LOREM IPSUM USED SINCE THE<br>1500S IS REPRODUCED BELOW<br>FOR THOSE INTERESTED.</p>
  <p class="abs cover-body">It is a long established fact that a reader will be distracted by the readable content of a page when looking at its layout. The point of using Lorem Ipsum is that it has a more-or-less normal distribution of letters, as opposed to using <strong>'Content here, content here',</strong> making it look like readable English.</p>
  <div class="abs dots"><i></i><i></i><i></i></div>

  <div class="photo-circle" role="img" aria-label="Photo of a suburban family home" style="left:18px;top:394px;width:68px;height:68px;background:linear-gradient(#bcd3e6 45%,#6f9a48 55%)"></div>
  <div class="photo-circle" role="img" aria-label="Photo of a modern house lit at dusk" style="left:78px;top:394px;width:68px;height:68px;background:linear-gradient(#2b3f86,#d9b64a 55%,#3a4f9a)"></div>
  <div class="photo-circle" role="img" aria-label="Photo of glass office towers" style="left:138px;top:394px;width:68px;height:68px;background:linear-gradient(135deg,#e6eef4,#6f8ea5 60%,#2e4c62)"></div>

  <div class="abs address">
    <h3>Address</h3>
    <p>Lorem Ipsum is not<br>simply random text.</p>
    <p>It has roots in a piece of<br>classical Latin literature,</p>
    <p class="phone">+00 00 0000 0000-00</p>
  </div>

  <p class="abs band-note"><strong>Can you help translate this site into a foreign language?</strong><br>Please email us with details if you can help.</p>
  <p class="abs grey-band-text"><strong>LOREM IPSUM HAS</strong><br>BEEN THE INDUSTRY'S</p>
  <p class="abs brand">KDR PROPERTY GROUP</p>
  <p class="abs cover-slogan"><span class="big condensed">SIMPLY<br>DUMMY TEXT</span><span class="small">OF THE PRINTING</span></p>
</section>

<section class="spread spread--inside">
  <svg class="spread__shapes" viewBox="0 0 1180 916" preserveAspectRatio="none">
    <defs>
      <linearGradient id="faint" x1="0" y1="0" x2="1" y2="1">
        <stop offset="0" stop-color="#f6f6f6"/><stop offset=".6" stop-color="#e8e8e8"/><stop offset="1" stop-color="#fbfbfb"/>
      </linearGradient>
      <linearGradient id="tower" x1="0" y1="0" x2="0" y2="1">
        <stop offset="0" stop-color="#3f86cc"/><stop offset=".35" stop-color="#a9c9e6"/><stop offset=".7" stop-color="#4a6f96"/><stop offset="1" stop-color="#c9c9c9"/>
      </linearGradient>
    </defs>
    <rect x="600" y="0" width="580" height="808" fill="url(#faint)" role="img" aria-label="Faint photo of a city building"/>
    <polygon points="0,0 205,0 240,118 0,830" fill="url(#tower)" role="img" aria-label="Photo of a residential tower against a blue sky"/>
    <polygon points="75,808 1180,808 1180,893 20,893" fill="var(--green-dark)"/>
  </svg>

  <h2 class="abs inside-title"><span class="light">Where</span><span class="bold">Does it come<br>from?</span></h2>
  <p class="abs inside-sub">Harold Penwick, a Latin<br>professor at Alderbrook<br>College in Virginia</p>
  <div class="abs inside-body">
    <p>Contrary to popular belief, Lorem Ipsum is not simply random text. It has roots in a piece of classical Latin literature from 45 BC, making it over 2000 years old. Harold Penwick, a Latin professor at Alderbrook College in Virginia, looked up one of the more obscure Latin words, consectetur, from a Lorem Ipsum passage, and going through the cites of the word in classical literature, discovered the undoubtable source. Lorem Ipsum comes from sections 1.10.32 and 1.10.33 of "de Finibus Bonorum et Malorum" (The Extremes of Good and Evil) by Varenus, written in 45 BC. This book is a treatise on the theory of ethics, very popular during the Renaissance. The first line of Lorem Ipsum, "Lorem ipsum dolor sit amet..", comes from a</p>
    <p class="last">line in section 1.10.32.</p>
  </div>
  <div class="abs donate">
    <h3>— DONATE: —</h3>
    <p>If you use this site regularly and would like to help keep the site on the Internet, please consider donating a small sum to help pay for the hosting and bandwidth bill. Paylio.</p>
  </div>

  <h2 class="abs col-title">THE STANDARD LOREM</h2>
  <p class="abs col-sub">Ipsum passage, used since the 1500s</p>
  <p class="abs quote">"Lorem ipsum dolor sit amet, consectetur adipiscing elit, sed do eiusmod tempor incididunt ut labore et dolore magna aliqua. Ut enim ad minim veniam, quis nostrud exercitation ullamco laboris nisi ut aliquip ex ea commodo consequat. Duis aute irure dolor in reprehenderit in voluptate velit esse cillum dolore eu fugiat nulla pariatur. Excepteur sint occaecat cupidatat non proident, sunt in culpa qui officia deserunt mollit anim id est laborum."</p>
  <ul class="abs bullets"><li>Paragraphs</li><li>Words</li><li>Bytes</li><li>Lists</li></ul>
  <p class="abs tagline">Lorem ipsum dolor sit amet...</p>
  <p class="abs col-para">Many desktop publishing packages and web page editors now use Lorem Ipsum as their default model text, and a search for 'lorem ipsum' will uncover many web sites still in their infancy. Various versions have.</p>

  <div class="photo-circle" role="img" aria-label="Photo of a high-rise office tower" style="left:585px;top:74px;width:138px;height:138px;background:linear-gradient(160deg,#f2f2f2,#6c6f86 50%,#3d3f52)"></div>
  <div class="photo-circle" role="img" aria-label="Photo of a home interior with a staircase" style="left:588px;top:196px;width:132px;height:132px;background:linear-gradient(#e9e6df,#9a6a42 60%,#5a3a24)"></div>
  <div class="photo-circle" role="img" aria-label="Photo of a two-storey house with garage" style="left:585px;top:312px;width:138px;height:138px;background:linear-gradient(#3e7fc6 30%,#e4d3b2 45%,#c9b08a 80%,#8c8c8c)"></div>

  <p class="abs col-close">There are now a set of mock banners<br>available here in three colours and in a range.</p>
  <p class="abs pay-band">click here to donate using Paylio. <strong>Thank you for your support.</strong></p>
</section>

</body>
</html>
```